Postcard Template

Background information:

ZEPRA Bright Tots is a socially progressive multi-national organization dedicated to getting more children more active. We offer a variety of exciting arts and fitness programs for children ages 1.5 to 12 years, held inside child care centers across Canada and in selected U.S. cities. Our programs are non-competitive, building children’s self-confidence, focus and creativity while having lots of fun.

Requirement:

We are looking for postcard templates that we will mail to prospective Child Care Centers, advising them of our programs. Colours should be bright and happy. Design should be attractive to businesses that work with children.

We need to be able to edit the text.

There will be 3 postcard campaigns during the year:
Fall (Back to School)
Winter/Spring Action
Summer Fun

Please provide designs for Fall (Back to School) campaign only.
The winning entry will be asked to provide templates for the other two campaigns.

Dimensions: 5.5” tall x 8.5” wide
Double-sided:
Mailing address label and stamp to be affixed to the back

Postcard Front Text:
ZEPRA Bright Tots logo
Exciting Arts & Fitness Programs for Child Care Centers
Fun Rolls In!
Bouncy Beat Moves
Tiny Stretch
Tot Drumline

Weekly or Bi-Weekly Classes
Single-time Workshops

Back to School Special: 4 one-hour workshops for the price of 3 (25% savings)
Book before December 31, 2013 for anytime until March 31, 2014.

Postcard Back Text:
ZEPRA Bright Tots logo
Fun Rolls In!
Great for Boys & Girls, Ages 1.5 to 12

Exciting dance, yoga and music programs
Weekly / Bi-Weekly Classes
Single-time Workshops
High interest / appeal to parents and children
Super fun delivery; strong educational content
Trained experienced instructors, all with background checks
Keeps enrollment high and waiting list strong
New revenue stream potential

For more information and to book, contact:
Marta
877-390-5162 ext 418
marta@zeprabright.example

Target Market(s)

Owners/operators of child care centers, catering to children ages 1.5 to 12 yrs old.

Industry/Entity Type

Progressive

Requirements
Must have
• 5.5 inches high x 8.5 inches wide

Highly visual front

Space for address label and stamp to be affixed on the back

Must be able to edit text (we have Illustrator) for different regions.

```html
<!DOCTYPE html>
<html lang="en">
<head>
<meta charset="utf-8">
<title>ZEPRA Bright Tots – Back to School Postcard</title>
<link href="https://fonts.googleapis.com/css2?family=Jost:wght@400;600;700&family=Questrial&display=swap" rel="stylesheet">
<style>
  :root{
    --page:#e9e9ea;
    --card:#ffffff;
    --navy:#2d4a7c;
    --navy-soft:#4d6a9c;
    --sky:#6f93cf;
    --red:#e4283a;
    --orange:#f1903a;
    --orange-light:#f6ad5f;
    --text-gray:#6b6b6b;
    --heading-blue:#2f4a78;
  }
  *{box-sizing:border-box;margin:0;padding:0}
  html,body{width:1200px;height:1200px;overflow:hidden;background:var(--page)}
  body{position:relative;font-family:"Questrial",sans-serif}
  .card{position:absolute;width:734px;height:475px;background:var(--card);box-shadow:0 2px 8px rgba(0,0,0,.18);overflow:hidden}
  .abs{position:absolute}

  /* back side */
  .card-back{left:370px;top:88px}
  .back-photo{left:0;top:23px;width:197px;height:154px;background:linear-gradient(135deg,#c9a58a,#e6cfb8 60%,#b9a28c)}
  .offer-tile{left:238px;top:23px;width:161px;height:154px;background:var(--orange)}
  .offer-tile .stripe{position:absolute;left:0;width:100%;height:7px;background:var(--orange-light)}
  .offer-tile h2{position:absolute;left:0;right:0;top:76px;text-align:center;font-family:"Jost",sans-serif;font-weight:600;color:#fff;font-size:19px}
  .offer-tile p{position:absolute;left:0;right:0;top:104px;text-align:center;font-family:"Jost",sans-serif;font-weight:600;color:#fff;font-size:13.5px;line-height:1.3}
  .brand{font-family:"Jost",sans-serif;font-weight:700;color:var(--red);white-space:nowrap}
  .back-brand{left:416px;top:42px;font-size:22px}
  .stamp-box{left:648px;top:22px;width:66px;height:64px;border:1.5px solid #b9b9b9}
  .feature-list{left:24px;top:190px;list-style:none;color:var(--text-gray);font-size:13.2px;line-height:14.4px;width:360px}
  .feature-list li{padding-left:10px;position:relative}
  .feature-list li::before{content:"•";position:absolute;left:0}
  .contact-rule{left:0;top:335px;width:399px;height:5px;background:var(--red)}
  .contact-band{left:0;top:340px;width:399px;height:82px;background:var(--navy-soft);color:#e3e9f4;text-align:center}
  .contact-band .lead{margin-top:12px;font-size:13px}
  .contact-band .name{font-size:19px;margin-top:1px}
  .contact-band .line{font-size:15px;margin-top:2px}

  /* front side */
  .card-front{left:98px;top:624px}
  .band-top{left:0;top:0;width:100%;height:24px;background:var(--navy)}
  .rule-top{left:0;top:24px;width:100%;height:5px;background:var(--red)}
  .rule-bottom{left:0;bottom:14px;width:100%;height:5px;background:var(--red)}
  .band-bottom{left:0;bottom:0;width:100%;height:14px;background:var(--navy)}
  .photo-main{left:0;top:32px;width:391px;height:198px;background:linear-gradient(135deg,#9fb3c9,#d8c2ae 45%,#7c8fb0)}
  .photo-left{left:0;top:235px;width:187px;height:115px;background:linear-gradient(135deg,#cdb79c,#e2d3c0 60%,#a8b9c8)}
  .photo-right{left:192px;top:235px;width:199px;height:115px;background:linear-gradient(135deg,#d3bea5,#efe4d6 55%,#8f9aa8)}
  .tagline-box{left:0;top:358px;width:394px;height:99px;background:linear-gradient(90deg,var(--sky) 0 12px,var(--navy) 12px);color:#fff;text-align:center}
  .tagline-box .sub{margin-top:10px;font-size:18px;line-height:1.25}
  .tagline-box .big{font-size:34px;margin-top:2px}
  .program-panel{left:406px;top:32px;width:298px;height:198px;background:#fff;display:flex;flex-direction:column;justify-content:center;align-items:center;gap:6px}
  .program-panel span{font-size:27px;color:var(--heading-blue)}
  .special-panel{left:406px;top:230px;width:298px;height:124px;background:var(--orange);color:#fff;text-align:center;padding-top:7px}
  .special-panel h3{font-family:"Jost",sans-serif;font-weight:600;font-size:17px;line-height:1.2}
  .special-panel p{font-size:13px;line-height:1.2}
  .special-panel h4{font-family:"Jost",sans-serif;font-weight:600;font-size:13px;line-height:1.2;margin-top:5px}
  .front-brand-panel{left:406px;top:358px;width:298px;height:99px;background:#fff;display:flex;align-items:center;justify-content:center}
  .front-brand-panel .brand{font-size:30px}
  .side-stripe-a{left:706px;top:32px;width:10px;height:425px;background:var(--sky)}
  .side-stripe-b{left:718px;top:32px;width:16px;height:425px;background:var(--navy-soft)}
</style>
</head>
<body>

<section class="card card-back" aria-label="Postcard back">
  <div class="abs back-photo" role="img" aria-label="Photo of two children dancing in a classroom"></div>
  <div class="abs offer-tile">
    <span class="stripe" style="top:0"></span>
    <span class="stripe" style="top:14px"></span>
    <span class="stripe" style="top:28px"></span>
    <span class="stripe" style="top:42px"></span>
    <h2>Fun Rolls In!</h2>
    <p>Great for Boys &amp; Girls,<br>Ages 1.5 to 12</p>
  </div>
  <div class="abs brand back-brand">ZEPRA Bright Tots</div>
  <div class="abs stamp-box" aria-label="Stamp area"></div>
  <ul class="abs feature-list">
    <li>Exciting dance, yoga and music programs</li>
    <li>Weekly / Bi-Weekly Classes</li>
    <li>Single-time Workshops</li>
    <li>High interest / appeal to parents and children</li>
    <li>Super fun delivery; strong educational content</li>
    <li>Trained experienced instructors, all with background checks</li>
    <li>Keeps enrollment high and waiting list strong</li>
    <li>New revenue stream potential</li>
  </ul>
  <div class="abs contact-rule"></div>
  <div class="abs contact-band">
    <p class="lead">For more information and to book, contact:</p>
    <p class="name">Marta</p>
    <p class="line">877-390-5162 ext 418 &nbsp;|&nbsp; marta@zeprabright.example</p>
  </div>
</section>

<section class="card card-front" aria-label="Postcard front">
  <div class="abs band-top"></div>
  <div class="abs rule-top"></div>
  <div class="abs photo-main" role="img" aria-label="Photo of children stretching in a circle with an instructor"></div>
  <div class="abs photo-left" role="img" aria-label="Photo of children dancing in a gym"></div>
  <div class="abs photo-right" role="img" aria-label="Photo of children playing drums with an instructor"></div>
  <div class="abs tagline-box">
    <p class="sub">Exciting Arts &amp; Fitness Programs<br>for Child Care Centers</p>
    <p class="big">Fun Rolls In!</p>
  </div>
  <div class="abs program-panel">
    <span>Bouncy Beat Moves</span>
    <span>Tiny Stretch</span>
    <span>Tot Drumline</span>
  </div>
  <div class="abs special-panel">
    <h3>Back to School Special:</h3>
    <p>4 one-hour workshops for the price of 3<br>(25% savings)</p>
    <h4>Book before:</h4>
    <p>December 31, 2013 for anytime<br>until March 31, 2014.</p>
  </div>
  <div class="abs front-brand-panel"><span class="brand">ZEPRA Bright Tots</span></div>
  <div class="abs side-stripe-a"></div>
  <div class="abs side-stripe-b"></div>
  <div class="abs rule-bottom"></div>
  <div class="abs band-bottom"></div>
</section>

</body>
</html>
```